Personal Tax Specialists Banner

We need banner adverts for a personal tax firm. We specialise in Luxembourg, US and UK personal taxation. The banner should be modern, cool, simple and illustrated.

Banner should highlight "Personal Taxation Specialists" and the countries that we specialise in, "Luxembourg", "US" and "UK".

Target Market(s)

Individuals looking for assistance with tax return preparation.

Industry/Entity Type

Finance And Accounting

Colors

Designer to choose colors to be used in the design.

Requirements
Must have
• Output in GIF.
• The main banner size is 980 x 120 and some smaller square banners (300 x 300)
• Button to link back to website www.quendrifin.com
Nice to have
• We would like an illustrated design if possible.

```html
<!DOCTYPE html>
<html lang="en">
<head>
<meta charset="utf-8">
<title>Quendri Tax &amp; Consulting – Personal Taxation Banners</title>
<link rel="stylesheet" href="https://fonts.googleapis.com/css2?family=Montserrat:wght@300;500;600;700&display=swap">
<style>
  :root {
    --maroon: #7a0034;
    --canvas-bg: #e6e6e6;
    --white: #ffffff;
    --gold: #f2b51c;
    --grey: #8c8c8c;
    --lux-red: #ef3340;
    --lux-blue: #27b2e6;
    --us-red: #c8102e;
    --us-blue: #2b3a8c;
    --uk-blue: #012169;
    --uk-red: #c8102e;
    --shadow: 6px 8px 10px rgba(0,0,0,0.35);
  }
  * { box-sizing: border-box; margin: 0; padding: 0; }
  html, body { width: 1200px; height: 650px; overflow: hidden; }
  body {
    background: var(--canvas-bg);
    font-family: "Montserrat", Arial, sans-serif;
    position: relative;
  }
  .banner {
    position: absolute;
    left: 69px;
    width: 1060px;
    height: 130px;
    background: var(--maroon);
    box-shadow: var(--shadow);
    overflow: hidden;
    color: var(--white);
  }
  .banner--headline { top: 49px; }
  .banner--services { top: 228px; }
  .banner--visit { top: 427px; }

  /* Headline banner */
  .brand-panel {
    position: absolute; left: 0; top: 0;
    width: 385px; height: 130px;
    background: linear-gradient(90deg, #ffffff 55%, #f6f1ee 100%);
    border-bottom-right-radius: 70px;
  }
  .brand-mark {
    position: absolute; left: 40px; top: 26px;
    width: 78px; height: 78px;
    border-radius: 50%;
    border: 3px solid #bdbdbd;
  }
  .brand-name {
    position: absolute; left: 134px; top: 30px;
    color: var(--maroon);
    font-weight: 500;
    line-height: 1;
  }
  .brand-name__main { display: block; font-size: 42px; letter-spacing: 1px; }
  .brand-name__sub { display: block; font-size: 16px; margin-top: 6px; letter-spacing: 0.5px; }
  .headline {
    position: absolute; left: 395px; right: 0; top: 18px;
    text-align: center;
    font-weight: 600;
    font-size: 42px;
    line-height: 48px;
    letter-spacing: 4px;
    text-transform: uppercase;
  }

  /* Services banner */
  .advisor-illustration {
    position: absolute; left: 26px; top: 16px;
    width: 126px; height: 100px;
    background: radial-gradient(circle at 35% 35%, var(--gold) 0 18%, transparent 19%),
                linear-gradient(160deg, #b07a4a 0%, #7a4a2a 100%);
    border-radius: 8px;
    opacity: 0.9;
  }
  .services-title {
    position: absolute; left: 182px; top: 0; height: 130px;
    display: flex; align-items: center;
    font-size: 40px; font-weight: 600; letter-spacing: 1px;
  }
  .country-panel {
    position: absolute; right: 0; top: 0;
    width: 491px; height: 130px;
    background: linear-gradient(90deg, #ffffff 0%, #f7f3f0 100%);
    border-bottom-left-radius: 70px;
  }
  .country {
    position: absolute; top: 22px;
    text-align: center;
  }
  .country--lux { left: 45px; width: 128px; }
  .country--usa { left: 187px; width: 134px; }
  .country--uk { left: 333px; width: 134px; }
  .country svg { display: block; width: 100%; height: 67px; }
  .country__label {
    display: block; margin-top: 12px;
    color: var(--maroon);
    font-size: 13px; font-weight: 700;
  }

  /* Visit banner */
  .globe-icon {
    position: absolute; left: 48px; top: 22px;
    width: 86px; height: 86px;
  }
  .visit-label {
    position: absolute; left: 178px; top: 0; height: 130px;
    display: flex; align-items: center;
    font-size: 40px; font-weight: 300; letter-spacing: 2px;
  }
  .visit-url {
    position: absolute; left: 397px; top: 0; height: 130px;
    display: flex; align-items: center;
    font-size: 56px; font-weight: 700;
  }
</style>
</head>
<body>

<section class="banner banner--headline">
  <div class="brand-panel">
    <span class="brand-mark"></span>
    <div class="brand-name">
      <span class="brand-name__main">QUENDRI</span>
      <span class="brand-name__sub">TAX &amp; CONSULTING</span>
    </div>
  </div>
  <h1 class="headline">Personal Taxation<br>Specialists</h1>
</section>

<section class="banner banner--services">
  <div class="advisor-illustration" role="img" aria-label="Illustration of a tax advisor in a brown suit beside a shining gold dollar coin"></div>
  <h2 class="services-title">OUR SERVICES</h2>
  <div class="country-panel">
    <div class="country country--lux">
      <svg viewBox="0 0 128 67" preserveAspectRatio="none" aria-hidden="true">
        <rect width="128" height="22" fill="var(--lux-red)"/>
        <rect y="22" width="128" height="23" fill="#ffffff"/>
        <rect y="45" width="128" height="22" fill="var(--lux-blue)"/>
      </svg>
      <span class="country__label">LUXEMBOURG</span>
    </div>
    <div class="country country--usa">
      <svg viewBox="0 0 134 67" preserveAspectRatio="none" aria-hidden="true">
        <defs>
          <pattern id="stripes" width="134" height="10.3" patternUnits="userSpaceOnUse">
            <rect width="134" height="5.15" fill="var(--us-red)"/>
            <rect y="5.15" width="134" height="5.15" fill="#ffffff"/>
          </pattern>
          <pattern id="stars" width="9" height="6" patternUnits="userSpaceOnUse">
            <circle cx="4.5" cy="3" r="1.2" fill="#ffffff"/>
          </pattern>
        </defs>
        <rect width="134" height="67" fill="url(#stripes)"/>
        <rect width="54" height="36" fill="var(--us-blue)"/>
        <rect width="54" height="36" fill="url(#stars)"/>
      </svg>
      <span class="country__label">USA</span>
    </div>
    <div class="country country--uk">
      <svg viewBox="0 0 60 30" preserveAspectRatio="none" aria-hidden="true">
        <rect width="60" height="30" fill="var(--uk-blue)"/>
        <path d="M0,0 L60,30 M60,0 L0,30" stroke="#ffffff" stroke-width="6"/>
        <path d="M0,0 L60,30 M60,0 L0,30" stroke="var(--uk-red)" stroke-width="2"/>
        <path d="M30,0 V30 M0,15 H60" stroke="#ffffff" stroke-width="10"/>
        <path d="M30,0 V30 M0,15 H60" stroke="var(--uk-red)" stroke-width="6"/>
      </svg>
      <span class="country__label">UK</span>
    </div>
  </div>
</section>

<section class="banner banner--visit">
  <svg class="globe-icon" viewBox="0 0 86 86" aria-hidden="true">
    <g fill="none" stroke="var(--gold)" stroke-width="4">
      <circle cx="43" cy="43" r="39"/>
      <ellipse cx="43" cy="43" rx="17" ry="39"/>
      <line x1="43" y1="4" x2="43" y2="82"/>
      <line x1="4" y1="43" x2="82" y2="43"/>
      <path d="M10 24 H76 M10 62 H76"/>
    </g>
  </svg>
  <span class="visit-label">VISIT US</span>
  <a class="visit-url" href="https://www.quendrifin.com" style="color:inherit;text-decoration:none">www.quendrifin.com</a>
</section>

</body>
</html>
```